Business Card Design

BBQ Concessions and Event Catering
Hi! My name is Dale I am looking for a biz card design for my BBQ company:
We specialize in ribs, brisket, pulled pork, chicken
Mainly Pork Product
Colors: Dark colors, Red, Black
Flames optional
This is a mobile trailer that moves to the party!
Copper Barn is a song by Lonnie Vasquell which influenced the name of my company. So I Love Blues and BBQ!
We also cater at music venues, parties, receptions etc. Anyone who needs good BBQ comes to us.

Looking forward to your designs.

Industry/Entity Type

Business

Contact Information for Business Card

Copper Barn BBQ, Dale Morrow Owner, 2718 Osgood Ave. LaPorte, In. 46912

```html
<!DOCTYPE html>
<html lang="en">
<head>
<meta charset="utf-8">
<title>Copper Barn BBQ – Business Card</title>
<link href="https://fonts.googleapis.com/css2?family=Alegreya+SC:wght@500;700&display=swap" rel="stylesheet">
<style>
  :root {
    --backdrop: #e9e4de;
    --card-red-deep: #5e0a10;
    --card-red: #7a1118;
    --card-red-light: #8c1a21;
    --ink-white: #fbf7f2;
    --shadow: rgba(40, 10, 10, 0.28);
  }
  html, body {
    margin: 0;
    padding: 0;
    width: 1200px;
    height: 675px;
    overflow: hidden;
    background: var(--backdrop);
  }
  .canvas {
    position: relative;
    width: 1200px;
    height: 675px;
    display: flex;
    align-items: center;
    justify-content: center;
  }
  .business-card {
    position: relative;
    width: 840px;
    height: 480px;
    border-radius: 4px;
    overflow: hidden;
    box-shadow: 0 18px 40px var(--shadow);
    color: var(--ink-white);
    font-family: "Alegreya SC", Georgia, serif;
  }
  .wood-backdrop {
    position: absolute;
    inset: 0;
    background: linear-gradient(100deg, var(--card-red-deep) 0%, var(--card-red) 45%, var(--card-red-light) 70%, var(--card-red-deep) 100%);
  }
  .card-content {
    position: relative;
    height: 100%;
    display: flex;
    flex-direction: column;
    align-items: center;
  }
  .brand-name {
    margin: 92px 0 0;
    font-size: 78px;
    font-weight: 700;
    letter-spacing: 1px;
    line-height: 1;
  }
  .owner-name {
    margin: 78px 0 0;
    font-size: 40px;
    font-weight: 700;
    letter-spacing: 1px;
    line-height: 1;
  }
  .owner-title {
    margin: 6px 0 0;
    font-size: 24px;
    font-weight: 500;
    letter-spacing: 1px;
    line-height: 1;
  }
  .address {
    margin: 22px 0 0;
    font-size: 18px;
    font-weight: 500;
    letter-spacing: 0.5px;
    line-height: 1;
  }
</style>
</head>
<body>
  <main class="canvas">
    <article class="business-card">
      <div class="wood-backdrop" role="img" aria-label="Dark red wood plank texture"></div>
      <div class="card-content">
        <h1 class="brand-name">Copper Barn BBQ</h1>
        <p class="owner-name">Dale Morrow</p>
        <p class="owner-title">Owner</p>
        <p class="address">2718 Osgood Ave La Porte, IN 46912</p>
      </div>
    </article>
  </main>
</body>
</html>
```